Golf Brochure + Business Card Design Project – Ridgeway Wellness.

Task Description

We are looking for a premium tri-fold brochure (8.5x11 letter, folded) plus a new business card design for Ridgeway Wellness. Both need to look polished, elegant, and professional — something that would feel at home in a golf club environment.

Brochure Scope:
• Tri-fold brochure promoting our new golf-specific services
• Incorporate brand colors: deep hunter green, cream, and gold accents
• Clean, modern typography (professional, not playful)
• Layout will follow the copy provided (final copy attached, no rewriting needed)
• Imagery: mature golfers (50+), golf lifestyle shots, no generic stocky images
• Include QR code placement linking to booking page
• Deliverables: print-ready PDF with bleed/crop (CMYK), high-res PDF (digital), and source file (InDesign or Illustrator)

Business Card Scope:
• Front + back design
• Consistent with brand colors and fonts
• Space for name, title, phone, email, and website
• Deliverables: print-ready PDF with bleed/crop (CMYK) + source file (AI or InDesign)
• If possible, provide editable template for future staff cards

Timeline:
• First draft within 5–7 days
• 2 rounds of revisions included

Budget:
$300 USD (total for both brochure + business card)

I’ll provide finalized copy if you accept the project.
Project description (paste this whole block in that box)

We need a premium tri-fold brochure (8.5”×11” letter, folded) and a new business card design for Ridgeway Wellness. This will be presented to golf course managers and members, so the look must be elegant, restrained, and country-club-classy.

Scope — Brochure
• Format: Tri-fold, 8.5”×11”. Please set 0.125” bleed on all sides and keep critical text ≥0.125–0.25” inside the trim.
• Purpose: Promote Ridgeway Wellness’ golf-specific services for adults 50+.
• Copy: We will provide finalized copy in a Word doc after acceptance. No rewriting needed — please focus on layout and polish.
• Imagery (required):
• Golf-first images (ball on tee/green, mature golfers mid-swing, and golf course landscapes at golden hour).
• 1–2 real Ridgeway Wellness gym photos on inside panels (trainer with client doing golf-relevant movement: stretch, rotation, balance).
• Visual style: Premium, quiet, lots of white/negative space, balanced grids; no clutter.
• Brand colors (required): Hunter Green #0C2E1F, Gold #CBA135, Cream #F5F2EB. Convert for CMYK print while preserving the look.
• Typography: Clean, legible serif + sans pairing (e.g., modern serif for headlines, humanist/neo-grotesk sans for body). You may propose suitable professional fonts; avoid playful/novelty fonts.
• Elements to include:
• Our logo (we will upload).
• QR code placement to booking page (we will supply the URL / QR asset).
• Simple icon treatment for the three complimentary options (Strength & Mobility, Stretch Therapy, Corvana + Assessment).
• Deliverables:
• Print-ready PDF (CMYK, with bleed & crop marks, PDF/X-1a or PDF/X-4)
• High-res digital PDF (no bleed)
• Source file (InDesign or Illustrator) + packaged fonts/links or outlined type as appropriate.

Scope — Business Card
• Size: 3.5”×2” (US standard) with 0.125” bleed; keep text ≥0.125” from trim.
• Front/back design; consistent with brochure branding.
• Fields: Name, Title, Phone, Email, Website, Address; optional small QR on back.
• Deliverables: Print-ready PDF (CMYK, bleed & crops) + Source file (AI/INDD). Provide an editable template for staff names.

Process & Timing
• Initial concept for brochure + card within 5–7 days of acceptance.
• 2 rounds of revisions included.
• Please start with a clean layout concept using placeholder images/text blocks; we’ll drop in final copy/assets immediately after acceptance.

Stock & Licensing
• You may propose stock images that fit the brief (we’re fine approving Pixelharbor or equivalent). Please note any license fees separately if needed.

Usage Rights
• We require full usage rights to the final designs for print & digital.

Target Market(s)

Golfers 50+ in Victoria, BC: quality-oriented, health-conscious, want to play longer, stronger, and pain-free. Country-club aesthetic; expect polished, professional materials.

Industry/Entity Type

Health & Fitness — Golf Performance / Longevity Studio

Font styles to use
Serif
Sans Serif

Requirements
Must have
• • Golf-first imagery + 1–2 real Ridgeway Wellness photos inside. • Brand colors: #0C2E1F (Hunter Green), #CBA135 (Gold), #F5F2EB (Cream). • Premium, restrained layout; ample negative space; no clutter. • Clean professional serif + sans type pairing; highly legible. • Space for logo and QR code (booking). • Correct print specs (bleed, crops, CMYK). • Deliverables: print-ready PDFs (brochure + card), digital PDF, source files.
Nice to have
• • Subtle texture or grain in backgrounds (very light) to add sophistication. • A second brochure cover variation (ball on tee vs. course landscape) at concept stage.
Should not have
• • Cheesy/posed “stocky” groups; overly young models; beer/alcohol imagery. • Over-saturated greens/blues; gimmicky gradients or clip art. • Generic fitness/bodybuilding shots unrelated to golf performance.

```html
<!DOCTYPE html>
<html lang="en">
<head>
<meta charset="utf-8">
<title>Ridgeway Wellness — Business Card, Front and Back</title>
<link rel="stylesheet" href="https://fonts.googleapis.com/css2?family=Nunito:wght@400;600;700&display=swap">
<style>
  :root {
    --backdrop: #9a9a9a;
    --card-green: #284241;
    --card-green-deep: #223a39;
    --emboss-tone: #35524f;
    --gold: #cba135;
    --edge-gold: #b8922c;
    --text-light: #e9ece9;
  }
  * { box-sizing: border-box; margin: 0; padding: 0; }
  html, body {
    width: 1200px;
    height: 1083px;
    overflow: hidden;
    background: var(--backdrop);
    font-family: "Nunito", sans-serif;
  }
  .sheet {
    width: 1200px;
    height: 1083px;
    display: flex;
    flex-direction: column;
    align-items: center;
    justify-content: center;
    gap: 40px;
  }
  .card {
    position: relative;
    width: 860px;
    height: 491px;
    background: var(--card-green);
    border-bottom: 3px solid var(--edge-gold);
    overflow: hidden;
  }
  .card--back { background: var(--card-green-deep); }

  /* Front */
  .contact {
    position: absolute;
    left: 64px;
    top: 92px;
    color: var(--text-light);
  }
  .contact__name {
    color: var(--gold);
    font-weight: 700;
    font-size: 29px;
    letter-spacing: 0.5px;
    text-transform: uppercase;
    line-height: 1.1;
  }
  .contact__title {
    font-size: 20px;
    margin-top: 4px;
  }
  .contact__address {
    font-size: 20px;
    line-height: 1.35;
    margin-top: 22px;
    font-style: normal;
  }
  .contact__list {
    list-style: none;
    margin-top: 22px;
    font-size: 20px;
    line-height: 1.5;
  }
  .contact__list li {
    display: flex;
    align-items: center;
    gap: 12px;
  }
  .contact__icon {
    width: 18px;
    height: 18px;
    flex: none;
  }
  .brand-mark {
    position: absolute;
    right: 56px;
    top: 50%;
    transform: translateY(-50%);
    display: flex;
    align-items: center;
    gap: 22px;
  }
  .brand-mark__dot {
    width: 54px;
    height: 54px;
    border-radius: 50%;
    background: var(--emboss-tone);
  }
  .brand-mark__name {
    color: var(--emboss-tone);
    font-weight: 700;
    font-size: 40px;
    line-height: 1.05;
    text-transform: uppercase;
    letter-spacing: 2px;
  }

  /* Back */
  .seal {
    position: absolute;
    left: 50%;
    top: 50%;
    transform: translate(-50%, -50%);
    display: flex;
    flex-direction: column;
    align-items: center;
    gap: 24px;
  }
  .seal__ring {
    width: 140px;
    height: 140px;
    border-radius: 50%;
    border: 3px solid var(--emboss-tone);
  }
  .seal__name {
    color: var(--emboss-tone);
    font-weight: 700;
    font-size: 30px;
    letter-spacing: 8px;
    text-transform: uppercase;
  }
</style>
</head>
<body>
<main class="sheet">

  <section class="card card--front" aria-label="Business card front">
    <div class="contact">
      <h1 class="contact__name">Daniel Whitmore</h1>
      <p class="contact__title">Development Manager Officer</p>
      <address class="contact__address">412 Harbour Lane<br>Suite 210, Victoria, BC V8W 1A2</address>
      <ul class="contact__list">
        <li>
          <svg class="contact__icon" viewBox="0 0 24 24" aria-hidden="true"><path fill="#cba135" d="M6.6 10.8a15.1 15.1 0 0 0 6.6 6.6l2.2-2.2c.3-.3.7-.4 1-.2 1.1.4 2.3.6 3.6.6.6 0 1 .4 1 1V20c0 .6-.4 1-1 1A17 17 0 0 1 3 4c0-.6.4-1 1-1h3.5c.6 0 1 .4 1 1 0 1.3.2 2.5.6 3.6.1.3 0 .7-.2 1z"/></svg>
          250-555-0147
        </li>
        <li>
          <svg class="contact__icon" viewBox="0 0 24 24" aria-hidden="true"><path fill="#cba135" d="M2 5h20v14H2z"/><path fill="none" stroke="#284241" stroke-width="1.8" d="M2.5 5.5 12 13l9.5-7.5"/></svg>
          daniel@ridgewaywell.co
        </li>
        <li>
          <svg class="contact__icon" viewBox="0 0 24 24" aria-hidden="true"><g fill="none" stroke="#cba135" stroke-width="1.6"><circle cx="12" cy="12" r="9.5"/><ellipse cx="12" cy="12" rx="4.2" ry="9.5"/><path d="M2.5 12h19M4 7h16M4 17h16"/></g></svg>
          ridgewaywell.co
        </li>
      </ul>
    </div>
    <div class="brand-mark">
      <span class="brand-mark__dot" aria-hidden="true"></span>
      <span class="brand-mark__name">Ridgeway<br>Wellness</span>
    </div>
  </section>

  <section class="card card--back" aria-label="Business card back">
    <div class="seal">
      <span class="seal__ring" aria-hidden="true"></span>
      <span class="seal__name">Ridgeway Wellness</span>
    </div>
  </section>

</main>
</body>
</html>
```